Business Card - Business Consultancy

Newly Established Company, specializing in Business Consultancy, Human Resource Management, Talent Acquisition and Payroll Solutions.

We need a Business card design which portrays "elegance" and a very sleek yet business-like design. We would like a nice blue trimming (which goes well with the logo) to separate the content of the business card at the top. We would also like to see the design using the color silver either as a background or incorporated into it.

The final design should be a Business card which has colors matching the logo; a nice font; the above-mentioned specifics that adheres to the theme of "a stylish and professional business"

FYI: please do not have too fanciful designs.

Industry/Entity Type

Business Consultant

Contact Information for Business Card

Darren Loh
Business Development Director
Opal Staffing Advisory Private Limited
27 Marlow Street, #05-03B
Crescent Harbour Tower
Singapore 061732
Mobile : (+65) 93584617
Email : dloh@opalstaffing-advisory.com
Alternative : opalstaffingadvisory@mailvista.com

Requirements
Must have
• Nice Blue Trimming matching Logo which separates content, see attached
• Design incorporates either a silver background or the use of the color silver
Should not have
• No Fanciful Designs
• No Childish Designs
• No Overly Complicated Designs

```html
<!DOCTYPE html>
<html lang="en">
<head>
<meta charset="utf-8">
<title>Opal Staffing Advisory – Business Card</title>
<link rel="stylesheet" href="https://fonts.googleapis.com/css2?family=Open+Sans:wght@400;600;700&family=Roboto:wght@700&display=swap">
<style>
  :root {
    --page-bg: #e9e9e9;
    --card-white: #ffffff;
    --trim-blue: #3d8fd8;
    --brand-blue: #3a8fd9;
    --brand-ink: #2b2f33;
    --tagline-grey: #6d7378;
    --panel-light: #4c5256;
    --panel-dark: #1f2224;
    --text-light: #f2f4f5;
  }
  * { margin: 0; padding: 0; box-sizing: border-box; }
  html, body {
    width: 1200px; height: 1000px; overflow: hidden;
    background: var(--page-bg);
  }
  .card {
    position: absolute; left: 230px; top: 289px;
    width: 740px; height: 423px;
    background: var(--card-white);
    box-shadow: 0 6px 18px rgba(0,0,0,0.18);
    overflow: hidden;
  }
  .brand {
    position: absolute; left: 92px; top: 56px;
    display: flex; align-items: center; gap: 22px;
  }
  .brand-mark {
    width: 84px; height: 84px; border-radius: 50%;
    background: var(--brand-blue);
  }
  .brand-name {
    font-family: "Roboto", sans-serif; font-weight: 700;
    font-size: 27px; line-height: 1.1; color: var(--brand-ink);
    width: 250px;
  }
  .brand-tagline {
    position: absolute; left: 213px; top: 144px;
    font-family: "Roboto", sans-serif; font-weight: 700;
    font-size: 8.5px; color: var(--tagline-grey); letter-spacing: 0.2px;
  }
  .trim {
    position: absolute; left: 0; top: 214px; width: 740px; height: 14px;
  }
  .panel {
    position: absolute; left: 0; top: 228px; width: 740px; height: 195px;
    background: radial-gradient(ellipse 60% 90% at 48% 40%, var(--panel-light), var(--panel-dark));
    font-family: "Open Sans", sans-serif; color: var(--text-light);
  }
  .person-name {
    position: absolute; left: 100px; top: 48px;
    font-size: 26px; font-weight: 600; color: var(--brand-blue);
  }
  .person-title {
    position: absolute; left: 107px; top: 93px;
    font-size: 10.5px;
  }
  .contact {
    position: absolute; left: 400px; top: 34px;
    display: grid; grid-template-columns: 80px auto;
    font-size: 13.5px; line-height: 18.5px;
  }
  .contact dt { font-weight: 700; }
  .contact dd.gap { margin-bottom: 12px; }
  .contact dt.gap { margin-bottom: 12px; }
</style>
</head>
<body>
  <div class="card">
    <div class="brand">
      <div class="brand-mark"></div>
      <div class="brand-name">Opal Staffing Advisory</div>
    </div>
    <div class="brand-tagline">Recruitment &nbsp;I&nbsp; HR Solutions I Business Consultancy</div>

    <svg class="trim" viewBox="0 0 740 14" preserveAspectRatio="none" aria-hidden="true">
      <defs>
        <pattern id="trim-teeth" width="14" height="14" patternUnits="userSpaceOnUse">
          <polygon points="0,7 7,1 14,7 14,14 0,14" fill="var(--trim-blue)"/>
        </pattern>
      </defs>
      <rect width="740" height="14" fill="url(#trim-teeth)"/>
    </svg>

    <div class="panel">
      <div class="person-name">Darren Loh</div>
      <div class="person-title">Business Development Director</div>
      <dl class="contact">
        <dt>Location</dt><dd>: 27 Marlow Street, #05-03B</dd>
        <dt></dt><dd>&nbsp;&nbsp;Crescent Harbour Tower</dd>
        <dt class="gap"></dt><dd class="gap">&nbsp;&nbsp;Singapore 061732</dd>
        <dt>Mobile</dt><dd>: (+65) 93584617</dd>
        <dt>Email</dt><dd>: dloh@opalstaffing-advisory.com</dd>
        <dt></dt><dd>: opalstaffingadvisory@mailvista.com</dd>
      </dl>
    </div>
  </div>
</body>
</html>
```